Business Cards for IT Consulting Company (Managed Service Provider)

I am looking to have some business cards printed and would like some designs. We are an IT Consulting company based in Vancouver BC. I would like a nice clean and modern look to the cards. I have uploaded all the versions of my logo so parts can be used as needed. Here is a snippit from our website homepage:

Kelbrook Systems Ltd. is an IT Solutions Partner located in Vancouver BC, Canada. We offer IT solutions and support to customers in the greater Vancouver Area. With expertise in Microsoft platforms, as well as Linux and Mac OSX and over 12 years experience in the IT industry, Kelbrook Systems is dedicated to offering our clients top quality service and products. We take pride in the solutions we offer our customers. The greatest compliment a client can give us is to recommend our services.

Kelbrook Systems Ltd. offers a wide range of IT services from onsite service to remote support and managed service solutions. This allows clients to choose the support path that best suits their company’s needs. Supporting many different sized companies from small to enterprise level over the past 12 years Kelbrook Systems has the experience and expertise needed to ensure things run smoothly. Allowing our clients to focus on doing business.

Revolutionizing the way IT services are delivered.

Kelbrook Systems is dedicated to providing our clients with IT solutions that work and grow with them for years to come. This philosophy helps save money in the long run instead of replacing equipment constantly. Far too often IT solutions are not well thought out and while possibly solving the problem at hand, require replacement due to growth or quality within a very short time frame. Kelbrook Systems takes pride in providing solutions that will last and be able to accommodate growth without the need for replacement.

Industry/Entity Type

Information Technology

Contact Information for Business Card

Kelbrook Systems Ltd.
(Employee Name)
Eml: (Employees Email Address)
Web: kelbrook.me
Ph: 604-555-0142

Font styles to use
Serif
Sans Serif

Requirements
Must have
• The Company logo and company colors.
Nice to have
• - Our tag line: "Building IT That Lasts" or "Revolutionizing the way IT services are delivered."
• - Also I really like the idea of nature and technology together blending which is sort of where my logo came from so integrating that somehow onto the business cards would be great.

```html
<!DOCTYPE html>
<html lang="en">
<head>
<meta charset="utf-8">
<title>Kelbrook Systems Ltd. — Business Card</title>
<link rel="stylesheet" href="https://fonts.googleapis.com/css2?family=Arimo:wght@400;700&family=Open+Sans:wght@700&display=swap">
<style>
  :root {
    --backdrop: #e9e7e3;
    --card-white: #ffffff;
    --card-grey: #5e5f61;
    --brand-blue: #18ade6;
    --text-white: #ffffff;
    --shadow: rgba(0, 0, 0, 0.22);
  }
  * { box-sizing: border-box; margin: 0; padding: 0; }
  html, body {
    width: 1200px;
    height: 950px;
    overflow: hidden;
    background: var(--backdrop);
    font-family: "Arimo", Arial, sans-serif;
  }
  .canvas {
    position: relative;
    width: 1200px;
    height: 950px;
  }
  .card {
    position: absolute;
    width: 620px;
    height: 354px;
    border-radius: 4px;
    overflow: hidden;
    box-shadow: 0 10px 28px var(--shadow);
  }

  /* Back of card */
  .card-back {
    left: 140px;
    top: 96px;
    background: var(--card-grey);
  }
  .card-back .brand {
    position: absolute;
    left: 0;
    right: 0;
    top: 118px;
    display: flex;
    justify-content: center;
    align-items: center;
    gap: 14px;
  }
  .brand-square {
    flex: none;
    width: 26px;
    height: 26px;
    border: 3px solid var(--brand-blue);
  }
  .card-back .brand-name {
    font-family: "Open Sans", Arial, sans-serif;
    font-weight: 700;
    font-size: 34px;
    color: var(--brand-blue);
    letter-spacing: 0.5px;
    white-space: nowrap;
  }
  .tagline {
    position: absolute;
    left: 0;
    right: 0;
    top: 236px;
    text-align: center;
    color: var(--text-white);
    font-size: 16px;
    letter-spacing: 0.6px;
  }

  /* Front of card */
  .card-front {
    left: 440px;
    top: 500px;
    background: var(--card-white);
  }
  .card-front .brand {
    position: absolute;
    left: 70px;
    top: 92px;
    display: flex;
    align-items: center;
    gap: 16px;
  }
  .card-front .brand-square {
    width: 40px;
    height: 40px;
    border-width: 4px;
  }
  .card-front .brand-name {
    font-family: "Open Sans", Arial, sans-serif;
    font-weight: 700;
    font-size: 40px;
    color: var(--brand-blue);
    letter-spacing: -0.5px;
    white-space: nowrap;
  }
  .contact-band {
    position: absolute;
    left: 0;
    right: 0;
    bottom: 0;
    height: 136px;
    background: var(--brand-blue);
    color: var(--text-white);
  }
  .person {
    position: absolute;
    left: 34px;
    top: 38px;
  }
  .person-name {
    font-weight: 700;
    font-size: 21px;
    margin-bottom: 8px;
  }
  .person-address {
    font-size: 15px;
    line-height: 20px;
  }
  .contact-list {
    position: absolute;
    right: 26px;
    top: 20px;
    list-style: none;
    text-align: right;
    font-size: 15px;
    line-height: 26px;
  }
  .contact-list li {
    display: flex;
    justify-content: flex-end;
    align-items: center;
    gap: 9px;
  }
  .contact-icon {
    width: 14px;
    height: 14px;
    fill: var(--text-white);
  }
</style>
</head>
<body>
<main class="canvas">

  <section class="card card-back" aria-label="Business card back">
    <div class="brand">
      <span class="brand-square"></span>
      <span class="brand-name">Kelbrook Systems</span>
    </div>
    <p class="tagline">Building IT That Lasts</p>
  </section>

  <section class="card card-front" aria-label="Business card front">
    <div class="brand">
      <span class="brand-square"></span>
      <span class="brand-name">Kelbrook Systems Ltd.</span>
    </div>

    <div class="contact-band">
      <div class="person">
        <p class="person-name">Marcus Hale</p>
        <p class="person-address">2190 Alder Crescent<br>Vancouver, BC V6K 2A1</p>
      </div>

      <ul class="contact-list">
        <li>604 555 0142
          <svg class="contact-icon" viewBox="0 0 16 16" aria-hidden="true">
            <path d="M3.6 1.2l2.2 2.4-1.2 1.8c.9 2 2.3 3.4 4.2 4.2l1.8-1.2 2.4 2.2-1.4 2.6C6.6 13 3 9.4 1.2 4.6z"/>
          </svg>
        </li>
        <li>marcus@kelbrook.me
          <svg class="contact-icon" viewBox="0 0 16 16" aria-hidden="true">
            <path d="M1 3h14v10H1z M1.8 3.8L8 8.6l6.2-4.8" fill="none" stroke="#fff" stroke-width="1.4"/>
            <path d="M1 3h14L8 8.4z"/>
          </svg>
        </li>
        <li>www.kelbrook.me
          <svg class="contact-icon" viewBox="0 0 16 16" aria-hidden="true">
            <circle cx="8" cy="8" r="6.5" fill="none" stroke="#fff" stroke-width="1.4"/>
            <ellipse cx="8" cy="8" rx="2.8" ry="6.5" fill="none" stroke="#fff" stroke-width="1.2"/>
            <path d="M1.5 8h13" stroke="#fff" stroke-width="1.2"/>
          </svg>
        </li>
      </ul>
    </div>
  </section>

</main>
</body>
</html>
```